Healthy Supplement featuring Moringa products

Need 3 business card options for our reps to order from Printwell. Our reps will be ordering from Printwell once we upload them. Attached is our current designs to show what info needs to be on the cards. Our website is www.tqvitality.com
The business cards will be a template for our reps to order from. Most of our reps are Asian & Hispanic. Please look at our website so you can see who we are to get the look and feel what we need.
Target Market(s)
Adults 30 on up. Health oriented people.
Industry/Entity Type
Health And Wellness
Contact Information for Business Card
Name
Title
Phone
Logo
www.tqvitality.com/my/username
Font styles to use
Requirements
Must have
- Please match our website look and colors. A moringa leaf is nice, but am open to something different.
Nice to have
- Healthy looking and warm, not super cold or too modern.
Should not have
- No harsh colors please.

```html
<!DOCTYPE html>
<html lang="en">
<head>
<meta charset="UTF-8">
<title>TQ Vitality Business Card</title>
<link rel="stylesheet" href="https://fonts.googleapis.com/css2?family=Arimo:wght@400;700&family=Open+Sans:wght@400;600&display=swap">
<style>
  :root {
    --backdrop: #3c3d40;
    --leaf-green: #6aaa45;
    --lime: #95c93d;
    --paper: #ffffff;
    --faint-leaf: #eef5e6;
    --shadow: rgba(0, 0, 0, 0.35);
  }
  * { margin: 0; padding: 0; box-sizing: border-box; }
  html, body {
    width: 1200px;
    height: 900px;
    overflow: hidden;
    background: var(--backdrop);
  }
  .stage {
    position: relative;
    width: 1200px;
    height: 900px;
  }
  .card {
    position: absolute;
    width: 630px;
    height: 360px;
    background: var(--paper);
    overflow: hidden;
    box-shadow: 0 14px 30px var(--shadow);
  }
  .card--front { left: 110px; top: 60px; }
  .card--back { left: 460px; top: 480px; }

  .leaf-decor {
    position: absolute;
    border-radius: 50%;
  }
  .card--front .leaf-decor {
    right: -40px;
    top: 20px;
    width: 390px;
    height: 250px;
    background: radial-gradient(ellipse at center, var(--faint-leaf) 0%, rgba(238,245,230,0.6) 55%, rgba(255,255,255,0) 75%);
  }
  .brand {
    position: absolute;
    display: flex;
    align-items: center;
    gap: 12px;
    font-family: "Open Sans", sans-serif;
    font-weight: 600;
    color: var(--leaf-green);
    white-space: nowrap;
  }
  .brand__dot {
    border-radius: 50%;
    background: var(--leaf-green);
  }
  .card--front .brand { left: 200px; top: 150px; font-size: 42px; }
  .card--front .brand__dot { width: 34px; height: 34px; }

  .card--back svg.back-art {
    position: absolute;
    inset: 0;
    width: 630px;
    height: 360px;
  }
  .card--back .leaf-decor {
    right: 30px;
    top: -20px;
    width: 200px;
    height: 240px;
    background: radial-gradient(ellipse at center, rgba(255,255,255,0.2) 0%, rgba(255,255,255,0.08) 55%, rgba(255,255,255,0) 75%);
  }
  .card--back .brand { right: 40px; top: 210px; font-size: 28px; }
  .card--back .brand__dot { width: 24px; height: 24px; }

  .contact {
    position: absolute;
    left: 36px;
    top: 38px;
    color: var(--paper);
    font-family: "Open Sans", sans-serif;
  }
  .contact__name {
    font-family: "Arimo", sans-serif;
    font-weight: 700;
    font-size: 30px;
    line-height: 1.1;
  }
  .contact__title {
    font-family: "Arimo", sans-serif;
    font-size: 23px;
    margin: 4px 0 0 12px;
  }
  .contact__location {
    margin: 16px 0 0 26px;
    font-size: 14px;
    line-height: 1.3;
  }
  .contact__list {
    list-style: none;
    margin: 14px 0 0 40px;
    font-size: 15px;
  }
  .contact__list li {
    display: flex;
    align-items: center;
    gap: 10px;
    line-height: 1.6;
    white-space: nowrap;
  }
  .contact__list svg { width: 13px; height: 13px; flex: none; }
</style>
</head>
<body>
<main class="stage">

  <section class="card card--front" aria-label="Business card front">
    <div class="leaf-decor" role="img" aria-label="Faint moringa leaf branch decoration"></div>
    <div class="brand"><span class="brand__dot"></span>TQ Vitality</div>
  </section>

  <section class="card card--back" aria-label="Business card back">
    <svg class="back-art" viewBox="0 0 630 360" aria-hidden="true">
      <rect width="630" height="360" fill="var(--leaf-green)"/>
      <path d="M190,360 C300,190 455,100 630,78 L630,92 C465,112 320,200 232,360 Z" fill="var(--paper)"/>
      <path d="M203,360 C310,197 460,106 630,88 L630,110 C470,128 332,215 245,360 Z" fill="var(--lime)"/>
      <path d="M245,360 C332,215 470,128 630,110 L630,360 Z" fill="var(--paper)"/>
    </svg>
    <div class="leaf-decor" role="img" aria-label="Soft moringa leaf decoration"></div>

    <div class="contact">
      <p class="contact__name">Dana Reyes</p>
      <p class="contact__title">Manager</p>
      <p class="contact__location">Location<br>Cedar Grove, California</p>
      <ul class="contact__list">
        <li>
          <svg viewBox="0 0 24 24"><path fill="#fff" d="M6.6 10.8a15.1 15.1 0 0 0 6.6 6.6l2.2-2.2a1 1 0 0 1 1-.25 11.4 11.4 0 0 0 3.6.57 1 1 0 0 1 1 1V20a1 1 0 0 1-1 1A17 17 0 0 1 3 4a1 1 0 0 1 1-1h3.5a1 1 0 0 1 1 1c0 1.25.2 2.45.57 3.6a1 1 0 0 1-.25 1z"/></svg>
          +1(909) 555-0142
        </li>
        <li>
          <svg viewBox="0 0 24 24"><path fill="#fff" d="M3 5h18v14H3zm2 2v.5l7 4.5 7-4.5V7l-7 4.5z"/></svg>
          info@tqvitality.com
        </li>
        <li>
          <svg viewBox="0 0 24 24"><circle cx="12" cy="12" r="9" fill="none" stroke="#fff" stroke-width="2"/><path d="M3 12h18M12 3c3 3 3 15 0 18M12 3c-3 3-3 15 0 18" fill="none" stroke="#fff" stroke-width="1.5"/></svg>
          www.tqvitality.com
        </li>
      </ul>
    </div>

    <div class="brand"><span class="brand__dot"></span>TQ Vitality</div>
  </section>

</main>
</body>
</html>
```